Website Ad for Commercial Real Estate Firm

I need to have three digital ads that would be similar theme to the ad that is attached. I'll need three of these with the sizes being:
728x90
300x100
300x250

Logos are attached and additional photos to be used for the ad along with text and contact information to include is at www.corbelhaynesre.com.

Target Market(s)

Commercial real estate owners and business owners

Industry/Entity Type

Real Estate

Requirements
Must have
• Contact information on each property division (commercial, property management, and residential).
Must include a variation of the ad in each of the three sizes.

```html
<!DOCTYPE html>
<html lang="en">
<head>
<meta charset="utf-8">
<title>Corbel-Haynes Real Estate — Display Ad Set</title>
<link rel="stylesheet" href="https://fonts.googleapis.com/css2?family=Noto+Serif:wght@400;700&display=swap">
<style>
  :root{
    --stage:#181818;
    --brand-green:#169c64;
    --brand-green-mid:#128556;
    --brand-green-dark:#006b3f;
    --ink:#1c1c1c;
    --white:#ffffff;
    --pill-text:#123d2b;
    --sky-top:#2f7fd6;
    --sky-low:#8cc0e8;
    --city-tone:#8a8a7e;
    --city-green:#4f6e3a;
  }
  *{margin:0;padding:0;box-sizing:border-box}
  html,body{width:1200px;height:1200px;overflow:hidden;background:var(--stage)}
  body{position:relative;font-family:"Noto Serif",Georgia,serif;color:var(--white)}

  .ad{position:absolute;background:var(--brand-green);overflow:hidden}
  .ad-leaderboard{left:97px;top:67px;width:1005px;height:124px}
  .ad-skyscraper{left:97px;top:245px;width:300px;height:899px}
  .ad-rectangle{left:448px;top:245px;width:612px;height:510px}

  .backdrop{position:absolute;inset:0;width:100%;height:100%}

  .brand{position:absolute;display:flex;align-items:center;white-space:nowrap}
  .brand-mark{border-radius:50%;background:var(--white);flex:none}
  .brand-name{font-weight:400;line-height:1;color:var(--white)}
  .brand-name .line-sub{display:block;letter-spacing:.28em;margin-top:4px}

  .tagline{position:absolute;white-space:nowrap;line-height:1;
    transform:scaleX(var(--sx,1));transform-origin:left top}
  .tagline-lead{color:var(--white);font-weight:400}
  .tagline-main{color:var(--ink);font-weight:400}

  .url-pill{position:absolute;background:var(--white);color:var(--pill-text);border-radius:999px;
    display:flex;align-items:center;justify-content:center;white-space:nowrap}

  .phone{position:absolute;display:flex;align-items:center;white-space:nowrap;font-weight:700;line-height:1}
  .phone svg{flex:none;margin-right:10px}

  /* leaderboard */
  .ad-leaderboard .brand{left:24px;top:21px}
  .ad-leaderboard .brand-mark{width:64px;height:64px;margin-right:10px}
  .ad-leaderboard .brand-name{font-size:33px}
  .ad-leaderboard .brand-name .line-sub{font-size:14px;padding-left:22px}
  .ad-leaderboard .phone{left:86px;top:90px;font-size:24px}
  .ad-leaderboard .tagline-lead{left:386px;top:20px;font-size:24px;--sx:.95}
  .ad-leaderboard .tagline-main{left:386px;top:45px;font-size:41px;--sx:.88}
  .ad-leaderboard .url-pill{left:414px;top:90px;width:275px;height:27px;font-size:16px}

  /* skyscraper */
  .ad-skyscraper .brand{left:16px;top:32px}
  .ad-skyscraper .brand-mark{width:58px;height:58px;margin-right:7px}
  .ad-skyscraper .brand-name{font-size:29px}
  .ad-skyscraper .brand-name .line-sub{font-size:13px;padding-left:20px}
  .ad-skyscraper .tagline-lead{left:21px;font-size:37px}
  .ad-skyscraper .lead-1{top:134px;--sx:.91}
  .ad-skyscraper .lead-2{top:178px;--sx:.92}
  .ad-skyscraper .tagline-main{left:20px;font-size:68px}
  .ad-skyscraper .main-1{top:219px;--sx:.94}
  .ad-skyscraper .main-2{top:287px;--sx:.85}
  .ad-skyscraper .url-pill{left:21px;top:367px;width:257px;height:38px;font-size:19px}
  .ad-skyscraper .phone{left:32px;top:418px;font-size:26px}

  /* rectangle */
  .ad-rectangle .brand{left:147px;top:29px}
  .ad-rectangle .brand-mark{width:70px;height:70px;margin-right:8px}
  .ad-rectangle .brand-name{font-size:40px}
  .ad-rectangle .brand-name .line-sub{font-size:17px;padding-left:26px}
  .ad-rectangle .tagline-lead{left:58px;top:123px;font-size:36px;--sx:.93}
  .ad-rectangle .tagline-main{left:57px;top:164px;font-size:58px;--sx:.93}
  .ad-rectangle .url-pill{left:59px;top:222px;width:220px;height:33px;font-size:15px}
  .ad-rectangle .phone{left:297px;top:224px;font-size:27px}
</style>
</head>
<body>

<!-- 728x90 leaderboard -->
<section class="ad ad-leaderboard" aria-label="Leaderboard ad">
  <svg class="backdrop" viewBox="0 0 1005 124" preserveAspectRatio="none">
    <defs>
      <linearGradient id="sky-lb" x1="0" y1="0" x2="0" y2="1">
        <stop offset="0" stop-color="var(--sky-top)"/>
        <stop offset=".45" stop-color="var(--sky-low)"/>
        <stop offset=".6" stop-color="var(--city-green)"/>
        <stop offset="1" stop-color="var(--city-tone)"/>
      </linearGradient>
    </defs>
    <g aria-hidden="true">
      <polygon points="717,0 790,0 767,82" fill="var(--brand-green-dark)"/>
      <polygon points="700,0 740,0 767,82" fill="var(--brand-green-mid)"/>
    </g>
    <g role="img" aria-label="Aerial photo of a downtown city skyline under blue sky">
      <polygon points="790,0 1005,0 1005,124 748,124" fill="url(#sky-lb)"/>
    </g>
  </svg>
  <div class="brand">
    <span class="brand-mark"></span>
    <span class="brand-name">Corbel-Haynes<span class="line-sub">REAL ESTATE</span></span>
  </div>
  <div class="phone">
    <svg width="22" height="22" viewBox="0 0 24 24" aria-hidden="true"><path fill="var(--white)" d="M6.6 10.8a15.1 15.1 0 0 0 6.6 6.6l2.2-2.2a1 1 0 0 1 1-.25 11.4 11.4 0 0 0 3.6.57 1 1 0 0 1 1 1V20a1 1 0 0 1-1 1A17 17 0 0 1 3 4a1 1 0 0 1 1-1h3.5a1 1 0 0 1 1 1c0 1.25.2 2.45.57 3.57a1 1 0 0 1-.25 1z"/></svg>
    (555) 214-3086
  </div>
  <p class="tagline tagline-lead">FOR EXPERTISE&amp; EXPERIENCE</p>
  <p class="tagline tagline-main">BEYOND COMPARE</p>
  <div class="url-pill">www.corbelhaynesre.com</div>
</section>

<!-- 300x600 skyscraper -->
<section class="ad ad-skyscraper" aria-label="Skyscraper ad">
  <svg class="backdrop" viewBox="0 0 300 899" preserveAspectRatio="none">
    <defs>
      <linearGradient id="sky-sk" x1="0" y1="0" x2="0" y2="1">
        <stop offset="0" stop-color="var(--sky-top)"/>
        <stop offset=".3" stop-color="var(--sky-low)"/>
        <stop offset=".55" stop-color="var(--city-tone)"/>
        <stop offset="1" stop-color="var(--city-green)"/>
      </linearGradient>
    </defs>
    <g aria-hidden="true">
      <polygon points="0,452 213,531 300,506 0,599" fill="var(--brand-green-mid)"/>
      <polygon points="0,474 165,545 0,599" fill="var(--brand-green-dark)"/>
    </g>
    <g role="img" aria-label="Aerial photo of downtown skyscrapers and tree-lined streets">
      <polygon points="0,599 300,506 300,899 0,899" fill="url(#sky-sk)"/>
    </g>
  </svg>
  <div class="brand">
    <span class="brand-mark"></span>
    <span class="brand-name">Corbel-Haynes<span class="line-sub">REAL ESTATE</span></span>
  </div>
  <p class="tagline tagline-lead lead-1">FOR EXPERTISE</p>
  <p class="tagline tagline-lead lead-2">&amp; EXPERIENCE</p>
  <p class="tagline tagline-main main-1">BEYOND</p>
  <p class="tagline tagline-main main-2">COMPARE</p>
  <div class="url-pill">www.corbelhaynesre.com</div>
  <div class="phone">
    <svg width="22" height="22" viewBox="0 0 24 24" aria-hidden="true"><path fill="var(--white)" d="M6.6 10.8a15.1 15.1 0 0 0 6.6 6.6l2.2-2.2a1 1 0 0 1 1-.25 11.4 11.4 0 0 0 3.6.57 1 1 0 0 1 1 1V20a1 1 0 0 1-1 1A17 17 0 0 1 3 4a1 1 0 0 1 1-1h3.5a1 1 0 0 1 1 1c0 1.25.2 2.45.57 3.57a1 1 0 0 1-.25 1z"/></svg>
    (555) 214-3086
  </div>
</section>

<!-- 300x250 rectangle -->
<section class="ad ad-rectangle" aria-label="Medium rectangle ad">
  <svg class="backdrop" viewBox="0 0 612 510" preserveAspectRatio="none">
    <defs>
      <linearGradient id="sky-rc" x1="0" y1="0" x2="0" y2="1">
        <stop offset="0" stop-color="var(--sky-top)"/>
        <stop offset=".55" stop-color="var(--sky-low)"/>
        <stop offset=".7" stop-color="var(--city-green)"/>
        <stop offset="1" stop-color="var(--city-tone)"/>
      </linearGradient>
    </defs>
    <g aria-hidden="true">
      <polygon points="0,255 329,311 612,263 0,365" fill="var(--brand-green-mid)"/>
      <polygon points="0,282 322,310 0,365" fill="var(--brand-green-dark)"/>
    </g>
    <g role="img" aria-label="Aerial photo of a downtown city skyline with a wooded horizon">
      <polygon points="0,365 612,263 612,510 0,510" fill="url(#sky-rc)"/>
    </g>
  </svg>
  <div class="brand">
    <span class="brand-mark"></span>
    <span class="brand-name">Corbel-Haynes<span class="line-sub">REAL ESTATE</span></span>
  </div>
  <p class="tagline tagline-lead">FOR EXPERTISE&amp; EXPERIENCE</p>
  <p class="tagline tagline-main">BEYOND COMPARE</p>
  <div class="url-pill">www.corbelhaynesre.com</div>
  <div class="phone">
    <svg width="22" height="22" viewBox="0 0 24 24" aria-hidden="true"><path fill="var(--white)" d="M6.6 10.8a15.1 15.1 0 0 0 6.6 6.6l2.2-2.2a1 1 0 0 1 1-.25 11.4 11.4 0 0 0 3.6.57 1 1 0 0 1 1 1V20a1 1 0 0 1-1 1A17 17 0 0 1 3 4a1 1 0 0 1 1-1h3.5a1 1 0 0 1 1 1c0 1.25.2 2.45.57 3.57a1 1 0 0 1-.25 1z"/></svg>
    (555) 214-3086
  </div>
</section>

</body>
</html>
```